Corvanel Website Homepage

Committed to delivering quality content, quillmarkwords.example is a content providing company. Equipped with resourceful writers with industry experience, we promise to empower our clients with content that is tailor-made to address specific requirements of their target Audience.

We need a website home page and one internal page designed. It is very important that the page be laid out with SEO in mind. We like the idea of using five images as navigation to our services. The five major services we offer are:
• Web Content writing (articles, features, website copy etc)
• Business Content writing (Press release, mailers & flyers, brochure/catalog)
• Personal Content writing (blog, speech writing)
• Hire a writer/editor
• Proof reading and editing services
The sample template (http://demo7.layoutsample.example/wt_48207/index.html) included has five images in the first fold. Designer can choose the right image for each service and lay over the service name on the image. Please do not use flash ( We will use javascripts). We need to have a detailed right side nav as in the template for SEO reasons. There will be some marketing ad- copy below the main images. Followed by a 200 character SEO optimized text defining our services in further detail. Apart from these a designer is free to use his creativity. The name of the site will be http://www.quillmarkwords.example/. This name will need a logo too. Please include it as part of design. Corvanelcorp is the owner of quillmarkwords.example. We already have a logo for Corvanel that is attached here as a separate file.

We have some taglines that need to be incorporated in the home page and other pages.
Please provide link button for Home, About us, Services, Samples, Pricing, Clients, Career, Contact us.

Links can be given on TOP, Sideways and Bottom and in the drop down menu of services etc.

Reason: Hi

We have made our project guaranteed and extended deadline by 5 days so you get more time to complete our project.

Thanks and Regards,

Ravindra Kulkarni
Corvanelcorp

Target Market(s)

Product Marketing Companies - Mostly in US.
Media companies which publish articles on various subjects. Travel and Lifestyle related sites, Educational Websites, Government Websites, Health related websites,

Industry/Entity Type

Marketing

Requirements
Must have
• Color of Homepage should blend with sober mood of the content. Writing Services should get highlighted in such a way that any person serious about the business visiting the site get attracted to read on the details of our content services. Most space should be used for details of writing services and links for our various pages and services. Webpage should be downloaded in lowest possible time.
Nice to have
• We have some idea about the website layouts;-http://www.pagefoundry.example/website-templates/48207.html - layout of information http://www.pagefoundry.example/website-templates/47915.html - for kind of marketing http://demo7.layoutsample.example/wt_48592/index.html - for colors
we attach a word file representing our idea in some way but not limited to it.
Should not have
• Gaudy (aggressive dark) colors. It should not be cluttered. No flash.

```html
<!DOCTYPE html>
<html lang="en">
<head>
<meta charset="utf-8">
<title>quillmarkwords.example — Content Writing Services</title>
<link href="https://fonts.googleapis.com/css2?family=Arimo:wght@400;700&display=swap" rel="stylesheet">
<style>
:root{
  --brand-red:#d8202a;
  --logo-red:#c8232c;
  --text:#6b6b6b;
  --link:#7a7a7a;
  --page:#ffffff;
  --header-top:#ffffff;
  --header-bottom:#ececec;
  --rule:#d6d6d6;
  --web:#c93a4c;
  --web-top:#d0414f;
  --business:#62b64c;
  --business-top:#58ad43;
  --personal:#e17b2c;
  --personal-top:#e9832f;
  --hire:#3b97c9;
  --hire-top:#2f86bd;
  --proof:#9d9d9d;
  --proof-top:#8e8e8e;
  --footer:#efefef;
}
*{box-sizing:border-box;margin:0;padding:0}
html,body{width:1148px;height:1200px;overflow:hidden}
body{background:var(--page);font-family:"Arimo",Arial,sans-serif;color:var(--text);position:relative}
a{color:inherit}

.site-header{position:absolute;left:0;top:0;width:1148px;height:118px;
  background:linear-gradient(var(--header-top),var(--header-bottom));
  border-top:6px solid var(--brand-red);border-bottom:1px solid var(--rule)}
.brand{position:absolute;left:154px;top:36px;font-size:31px;color:var(--logo-red);text-decoration:none;letter-spacing:-.2px}
.main-nav{position:absolute;left:704px;top:-6px;display:flex}
.main-nav a{display:block;height:56px;line-height:56px;padding:0 13px;font-size:16px;color:#333;text-decoration:none;margin-right:2px}
.main-nav a.is-current{background:var(--brand-red);color:#fff;border-radius:0 0 4px 4px}

.hero-strip{position:absolute;left:53px;top:121px;width:1043px;height:348px;display:flex}
.hero-strip div{flex:1}
.hero-1{background:linear-gradient(135deg,#e8ecef,#9aa3aa 60%,#3a3f44)}
.hero-2{background:linear-gradient(160deg,#f2f2f2,#c8b4a6 50%,#2b2b2b)}
.hero-3{background:linear-gradient(180deg,#6e5a44,#a09070 45%,#7e8a96)}
.hero-4{background:linear-gradient(180deg,#4f8a7c,#5a83b5 60%,#38527a)}
.hero-5{background:linear-gradient(150deg,#dcdcdc,#a8a8a8 55%,#5a5a5a)}

.intro-copy{position:absolute;left:67px;top:502px;width:548px;font-size:12px;line-height:18.7px}
.portrait{position:absolute;left:631px;top:483px;width:188px;height:230px;border:1px solid var(--rule);padding:3px;background:#fff}
.portrait div{width:100%;height:100%;background:linear-gradient(180deg,#f4f4f4,#c9a58a 55%,#1f2630)}

.side-nav{position:absolute;left:843px;top:481px;width:253px;height:232px;border:1px solid var(--rule);background:#f6f6f6;padding:7px 0 0 18px;list-style:none}
.side-nav li{height:27.2px;display:flex;align-items:center;font-size:13px;color:var(--link)}
.side-nav svg{margin-right:14px}
.side-nav a{text-decoration:underline}

.services{position:absolute;left:53px;top:737px;width:1043px;height:316px;display:flex}
.service{flex:1;color:#fff;position:relative;border-top:6px solid;padding:14px 9px 0 9px}
.service h2{font-size:14.5px;line-height:18.5px;font-weight:700;text-transform:uppercase;height:46px;display:flex;align-items:center;padding-left:1px}
.service h2.small{font-size:12.5px}
.service hr{border:0;border-top:1px dashed rgba(255,255,255,.75);margin:3px 0 16px}
.service p{font-size:12px;line-height:18.8px;text-align:justify;padding:0 7px}
.read-more{position:absolute;left:11px;top:267px;height:28px;display:flex;align-items:center;border-radius:5px;background:rgba(0,0,0,.2);font-size:12.5px;font-weight:700;text-decoration:none;padding:0 0 0 10px}
.read-more span{margin-left:8px;border-left:1px solid rgba(255,255,255,.4);padding:0 7px;height:100%;display:flex;align-items:center}
.service.web{background:var(--web);border-color:var(--web-top)}
.service.business{background:var(--business);border-color:var(--business-top)}
.service.personal{background:var(--personal);border-color:var(--personal-top)}
.service.hire{background:var(--hire);border-color:var(--hire-top)}
.service.proof{background:var(--proof);border-color:var(--proof-top)}

.site-footer{position:absolute;left:0;top:1094px;width:1148px;height:106px;border-top:1px solid var(--rule);background:#f8f8f8}
.footer-nav{position:absolute;left:405px;top:8px;font-size:12.5px;color:#8a8a8a;display:flex;gap:16px}
.footer-nav a{text-decoration:none}
.footer-band{position:absolute;left:53px;top:28px;width:1043px;height:62px;background:linear-gradient(var(--footer),#f6f6f6)}
.copyright{position:absolute;left:4px;top:15px;font-size:12px;color:#8a8a8a}
.social{position:absolute;right:6px;top:14px;display:flex;gap:6px}
.social span{width:20px;height:20px;border-radius:3px}
</style>
</head>
<body>
<header class="site-header">
  <a class="brand" href="#">quillmarkwords.example</a>
  <nav class="main-nav">
    <a class="is-current" href="#">HOME</a>
    <a href="#">ABOUT US</a>
    <a href="#">SERVICES</a>
    <a href="#">CONTACT US</a>
  </nav>
</header>

<section class="hero-strip">
  <div class="hero-1" role="img" aria-label="Photo: hands at a laptop keyboard holding a clipboard"></div>
  <div class="hero-2" role="img" aria-label="Photo: businesswoman writing at a desk"></div>
  <div class="hero-3" role="img" aria-label="Photo: student writing in front of bookshelves"></div>
  <div class="hero-4" role="img" aria-label="Photo: professional in shirt and tie with a pen"></div>
  <div class="hero-5" role="img" aria-label="Photo: desk with mouse, glasses and pen"></div>
</section>

<p class="intro-copy">Lorem ipsum dolor sit amet, consectetuer adipiscing elit. Aenean commodo ligula eget dolor. Aenean massa. Cum sociis natoque penatibus et magnis dis parturient montes, ridiculus mus. Donec quam felis, ultricies nec, pellentesque eu, pretium quis, sem. Nulla conquat massa quis enim. Donec pede justo, fringilla vel, aliquet nec, vulputate eget, arcu. In enim justo, rhonc ut, imperdiet a, venenatis vitae, justo. Nullam dictum felis eu pede mollis pr Integer tincidunttt. Cras dapibus.Lorem ipsum dolor sit amet, consectetuer adipiscing elit. Aenean commodo ligula eget dolor. Aenean massa. Cum sociis natoque penatibus et magni parturient montescetur ridiculus mus. Donec quam felis, ultricies nec, pellentesque eu, pretium quis,</p>

<div class="portrait"><div role="img" aria-label="Photo: smiling writer in a suit"></div></div>

<ul class="side-nav">
  <li><svg width="6" height="9" viewBox="0 0 6 9"><path d="M1 1l3.5 3.5L1 8" fill="none" stroke="#777" stroke-width="1.2"/></svg><a href="#">Lorem ipsum dolor sit amet,</a></li>
  <li><svg width="6" height="9" viewBox="0 0 6 9"><path d="M1 1l3.5 3.5L1 8" fill="none" stroke="#777" stroke-width="1.2"/></svg><a href="#">Lorem ipsum dolor sit amet,</a></li>
  <li><svg width="6" height="9" viewBox="0 0 6 9"><path d="M1 1l3.5 3.5L1 8" fill="none" stroke="#777" stroke-width="1.2"/></svg><a href="#">Lorem ipsum dolor sit amet,</a></li>
  <li><svg width="6" height="9" viewBox="0 0 6 9"><path d="M1 1l3.5 3.5L1 8" fill="none" stroke="#777" stroke-width="1.2"/></svg><a href="#">Lorem ipsum dolor sit amet,</a></li>
  <li><svg width="6" height="9" viewBox="0 0 6 9"><path d="M1 1l3.5 3.5L1 8" fill="none" stroke="#777" stroke-width="1.2"/></svg><a href="#">Lorem ipsum dolor sit amet,</a></li>
  <li><svg width="6" height="9" viewBox="0 0 6 9"><path d="M1 1l3.5 3.5L1 8" fill="none" stroke="#777" stroke-width="1.2"/></svg><a href="#">Lorem ipsum dolor sit amet,</a></li>
  <li><svg width="6" height="9" viewBox="0 0 6 9"><path d="M1 1l3.5 3.5L1 8" fill="none" stroke="#777" stroke-width="1.2"/></svg><a href="#">Lorem ipsum dolor sit amet,</a></li>
  <li><svg width="6" height="9" viewBox="0 0 6 9"><path d="M1 1l3.5 3.5L1 8" fill="none" stroke="#777" stroke-width="1.2"/></svg><a href="#">Lorem ipsum dolor sit amet,</a></li>
</ul>

<section class="services">
  <article class="service web">
    <h2>Web Content<br>Writing</h2><hr>
    <p>Lorem ipsum dolor sit amet, consectetuer adipiscing elit. Aenean commodo ligula eget dolor. Aenean massa. Cum sociis natoque penatibus-Lorem ipsum dolor sit amet, consectetuer d bbdiscvhsi-uvdsfvsvrpenatibus</p>
    <a class="read-more" href="#">READ MORE<span>&gt;&gt;</span></a>
  </article>
  <article class="service business">
    <h2>Business Content<br>Writing</h2><hr>
    <p>Lorem ipsum dolor sit amet, consectetuer adipiscing elit. Aenean commodo ligula eget dolor. Aenean massa. Cum sociis natoque penatibus-Lorem ipsum dolor sit amet, consectetuer d bbdiscvhsi-uvdsfvsvrpenatibus</p>
    <a class="read-more" href="#">READ MORE<span>&gt;&gt;</span></a>
  </article>
  <article class="service personal">
    <h2 class="small">Personal Content<br>Writing</h2><hr>
    <p>Lorem ipsum dolor sit amet, consectetuer adipiscing elit. Aenean commodo ligula eget dolor. Aenean massa. Cum sociis natoque penatibus-Lorem ipsum dolor sit amet, consectetuer d bbdiscvhsi-uvdsfvsvrpenatibus</p>
    <a class="read-more" href="#">READ MORE<span>&gt;&gt;</span></a>
  </article>
  <article class="service hire">
    <h2>Hire a Writer/Editor</h2><hr>
    <p>Lorem ipsum dolor sit amet, consectetuer adipiscing elit. Aenean commodo ligula eget dolor. Aenean massa. Cum sociis natoque penatibus-Lorem ipsum dolor sit amet, consectetuer d bbdiscvhsi-uvdsfvsvrpenatibus</p>
    <a class="read-more" href="#">READ MORE<span>&gt;&gt;</span></a>
  </article>
  <article class="service proof">
    <h2>Proof Reading and<br>Editing Services</h2><hr>
    <p>Lorem ipsum dolor sit amet, consectetuer adipiscing elit. Aenean commodo ligula eget dolor. Aenean massa. Cum sociis natoque penatibus-Lorem ipsum dolor sit amet, consectetuer d bbdiscvhsi-uvdsfvsvrpenatibus</p>
    <a class="read-more" href="#">READ MORE<span>&gt;&gt;</span></a>
  </article>
</section>

<footer class="site-footer">
  <nav class="footer-nav">
    <a href="#">HOME</a><span>|</span><a href="#">ABOUT US</a><span>|</span><a href="#">SERVICES</a><span>|</span><a href="#">CONTACT US</a>
  </nav>
  <div class="footer-band">
    <p class="copyright">Copyright @ 2011 quillmarkwords.example - All Right Reserved</p>
    <div class="social">
      <span style="background:#e8772a" role="img" aria-label="Feed link"></span>
      <span style="background:#45b0e3" role="img" aria-label="Social link"></span>
      <span style="background:#3b5a9a" role="img" aria-label="Social link"></span>
      <span style="background:#c9302c" role="img" aria-label="Video link"></span>
    </div>
  </div>
</footer>
</body>
</html>
```